Sunny Circle Card

4x6 Referral card double sided

basic hand drawn outline attached
not meant to be interpreted exactly but use artistic license to create what you think is best

Logo images uploaded as well

The purpose of this card is to have existing clients refer others to our office and have both of them get rewarded, however we wont put in writing that the original person gets rewarded - rather we will tell them verbally

```html
<!DOCTYPE html>
<html lang="en">
<head>
<meta charset="utf-8">
<title>Sunny Circle Referral Card</title>
<link rel="stylesheet" href="https://fonts.googleapis.com/css2?family=Cinzel:wght@700;800&family=Rubik:wght@400;700&family=Oswald:wght@700&family=Poppins:wght@400;500;600&display=swap">
<style>
  :root {
    --backdrop: #4a4746;
    --card-wash: #eaf7fa;
    --card-wash-deep: #cdeef4;
    --brand-blue: #1389b8;
    --navy: #0f1c33;
    --ink: #1a2233;
    --olive-rule: #b9c48a;
    --leaf-teal: #5fb7c2;
    --leaf-gold: #e3bc43;
    --leaf-plum: #6b6177;
    --sky-photo: #7cc4e0;
    --logo-green: #3d8b2f;
    --white: #ffffff;
  }
  * { box-sizing: border-box; margin: 0; padding: 0; }
  html, body { width: 1003px; height: 1200px; overflow: hidden; }
  body { background: var(--backdrop); position: relative; font-family: "Poppins", sans-serif; }

  .card {
    position: absolute; left: 201px; width: 602px; height: 401px; overflow: hidden;
    background:
      radial-gradient(ellipse at 30% 70%, var(--card-wash-deep) 0%, transparent 55%),
      radial-gradient(ellipse at 75% 30%, #d6f1f6 0%, transparent 50%),
      var(--card-wash);
    box-shadow: 0 8px 22px rgba(0,0,0,.35);
  }
  .card--front { top: 133px; }
  .card--back { top: 658px; }

  .foliage { position: absolute; }
  .foliage--front-left { left: 0; top: 0; width: 130px; height: 170px;
    background: radial-gradient(ellipse at 0 0, var(--leaf-teal) 0%, rgba(227,188,67,.55) 35%, transparent 70%); }
  .foliage--front-right { right: 0; top: 0; width: 260px; height: 160px;
    background: radial-gradient(ellipse at 90% 0, rgba(95,183,194,.85) 0%, rgba(95,183,194,.35) 45%, transparent 72%); }
  .foliage--back-left { left: 0; top: 0; width: 200px; height: 140px;
    background: radial-gradient(ellipse at 20% 0, var(--leaf-gold) 0%, rgba(95,183,194,.7) 35%, transparent 72%); }
  .foliage--back-right { right: 0; top: 0; width: 270px; height: 170px;
    background: radial-gradient(ellipse at 75% 0, rgba(107,97,119,.85) 0%, rgba(95,183,194,.7) 30%, rgba(227,188,67,.4) 50%, transparent 75%); }

  .brand { position: absolute; display: flex; flex-direction: column; align-items: center; width: 160px; }
  .brand__mark { width: 44px; height: 44px; border-radius: 50%; background: var(--logo-green); }
  .brand__name { margin-top: 8px; font-family: "Cinzel", serif; font-weight: 700; font-size: 20px; color: var(--brand-blue); letter-spacing: 1px; white-space: nowrap; }
  .card--front .brand { left: 102px; top: 36px; }
  .card--back .brand { left: 221px; top: 36px; }

  .headline { position: absolute; left: 0; width: 362px; text-align: center; font-family: "Cinzel", serif; font-weight: 800; line-height: 1; }
  .headline--top { top: 146px; font-size: 46px; color: var(--brand-blue); }
  .headline--bottom { top: 193px; font-size: 49px; color: var(--navy); }

  .offer { position: absolute; left: 49px; top: 256px; width: 262px; height: 85px;
    border-top: 1px solid var(--olive-rule); border-bottom: 1px solid var(--olive-rule); }
  .offer__label { position: absolute; left: 2px; top: 6px; font-family: "Rubik", sans-serif; font-size: 19px; line-height: 23.5px; color: var(--navy); font-weight: 700; }
  .offer__label .light { font-weight: 400; }
  .offer__amount { position: absolute; left: 148px; top: -2px; font-family: "Oswald", sans-serif; font-weight: 700; font-size: 70px; line-height: 1.15; color: var(--brand-blue); letter-spacing: -1px; }

  .photo { position: absolute; left: 320px; top: 50px; width: 282px; height: 351px; }

  .field { position: absolute; left: 33px; right: 35px; display: flex; align-items: flex-end; gap: 6px;
    font-weight: 600; font-size: 12.5px; letter-spacing: 3px; color: var(--ink); }
  .field__line { flex: 1; border-bottom: 1.5px dotted var(--ink); margin-bottom: 3px; }
  .field--referrer { top: 164px; }
  .field--patient { top: 208px; }

  .contact { position: absolute; top: 255px; left: 0; width: 100%; height: 34px; }
  .contact__phone { position: absolute; left: 75px; top: 4px; display: flex; align-items: center; gap: 7px;
    font-weight: 600; font-size: 21px; color: var(--ink); }
  .contact__divider { position: absolute; left: 300px; top: 0; width: 1.5px; height: 30px; background: var(--brand-blue); }
  .contact__address { position: absolute; left: 327px; top: 0; display: flex; gap: 7px; font-size: 13.5px; line-height: 17px; color: var(--ink); }

  .web-pill { position: absolute; left: 108px; top: 310px; width: 387px; height: 25px; border-radius: 13px;
    background: var(--brand-blue); color: var(--white); text-align: center; font-weight: 500; font-size: 13.5px; line-height: 25px; letter-spacing: 3px; }
  .instruction { position: absolute; left: 0; width: 100%; top: 346px; text-align: center; font-weight: 600; font-size: 12.5px; letter-spacing: 3.4px; color: var(--ink); }
</style>
</head>
<body>

<section class="card card--front">
  <div class="foliage foliage--front-left" role="img" aria-label="Watercolor tropical leaves in teal, gold and plum"></div>
  <div class="foliage foliage--front-right" role="img" aria-label="Watercolor blue monstera and palm leaves"></div>

  <div class="brand">
    <span class="brand__mark"></span>
    <span class="brand__name">SUNNY CIRCLE</span>
  </div>

  <h1 class="headline headline--top">SPREAD</h1>
  <h1 class="headline headline--bottom">THE SMILE</h1>

  <div class="offer">
    <p class="offer__label">YOUR FRIENDS<br><span class="light">OR</span> FAMILY<br>RECIEVES</p>
    <p class="offer__amount">$25</p>
  </div>

  <svg class="photo" viewBox="0 0 282 351" role="img" aria-label="Photo of three smiling women taking a selfie by the sea">
    <defs>
      <linearGradient id="photoTone" x1="0" y1="0" x2="0" y2="1">
        <stop offset="0" stop-color="#9fd6ea"/>
        <stop offset=".55" stop-color="#3f8fb8"/>
        <stop offset="1" stop-color="#22324a"/>
      </linearGradient>
    </defs>
    <circle cx="154" cy="243" r="146" fill="none" stroke="#a9dcea" stroke-width="3"/>
    <circle cx="154" cy="243" r="143" fill="url(#photoTone)"/>
    <rect x="60" y="0" width="222" height="140" fill="url(#photoTone)" opacity=".0"/>
  </svg>
</section>

<section class="card card--back">
  <div class="foliage foliage--back-left" role="img" aria-label="Watercolor tropical leaves in gold, teal and plum"></div>
  <div class="foliage foliage--back-right" role="img" aria-label="Watercolor tropical leaves in plum, teal and gold"></div>

  <div class="brand">
    <span class="brand__mark"></span>
    <span class="brand__name">SUNNY CIRCLE</span>
  </div>

  <div class="field field--referrer"><span>YOUR NAME</span><span class="field__line"></span></div>
  <div class="field field--patient"><span>NEW PATIENT NAME</span><span class="field__line"></span></div>

  <div class="contact">
    <div class="contact__phone">
      <svg width="15" height="15" viewBox="0 0 16 16" aria-hidden="true">
        <circle cx="8" cy="8" r="8" fill="var(--logo-green)"/>
        <path d="M5.2 4.2l1.3-.3.8 1.8-.9.8a5 5 0 0 0 2.2 2.2l.8-.9 1.8.8-.3 1.3c-3.4.3-6-2.3-5.7-5.7z" fill="#fff"/>
      </svg>
      <span>555 - 014 - 2288</span>
    </div>
    <span class="contact__divider"></span>
    <div class="contact__address">
      <svg width="11" height="13" viewBox="0 0 11 13" aria-hidden="true" style="margin-top:1px">
        <path d="M5.5 0.5a4 4 0 0 1 4 4c0 2.6-4 6.3-4 6.3s-4-3.7-4-6.3a4 4 0 0 1 4-4z" fill="var(--logo-green)"/>
        <circle cx="5.5" cy="4.5" r="1.5" fill="#fff"/>
        <rect x="0.5" y="11.5" width="10" height="1.2" fill="var(--logo-green)"/>
      </svg>
      <p>1200 Harbor Lane<br>Palm Grove, FL 33000</p>
    </div>
  </div>

  <div class="web-pill">www.sunnycircledental.com</div>
  <p class="instruction">HAVE THEM BRING THIS CARD TO THEIR FIRST VISIT!</p>
</section>

</body>
</html>
```